Oral Surgery Office Referral Form and Stationary designs.

Hi, I am a dentist/oral surgeon recently graduated and starting my own practice. Need help in designing an attractive, warm, appealing and Professional referral form (double sided), and stationary design. These will be used for Thank you notes, Professional letters, Front of a presentation folder, Notepads, envelopes, promotional products, Fax, etc... I do have a sample of a typical referral form and also have a logo as well as business card design that I will provide as a base to use. I will attach the files to this posting. Please, do some investigating on the Oral surgery / dental specialist websites as to some of the examples of the referral forms. Thanks and feel free to respond with any questions. Look forward to the designs - having the business card designed here was a great experience.
I will attach more files to clarify / show examples.

HELLO ALL,

I JUST WENT THROUGH THE BRIEF AND REALISED THAT THERE IS A MISTAKE IN MY POSTING. 
THE WEBSITE ADDRESS SHOULD READ:
 WWW.KRELDAX.COM 
IN MY ORIGINAL POSTING IT WAS MISSING THE "M".

TRULY APOLOGIZE FOR ANY INCONVENIENCE.
THANK YOU,
GERALD

Target Market(s)

Dental Professionals and oral surgery patients.

Industry/Entity Type

Dental

Requirements
Must have
• Has to have pictures of the mouth / teeth numbers/ map with directions. Needs to be warm and appealing. If possible to have it in a format that can be easily converted to a clickable one online. Don't know if possible. Thanks.
Should not have
• Typical dental designs .

```html
<!DOCTYPE html>
<html lang="en">
<head>
<meta charset="utf-8">
<title>Harlow Creek Oral Surgery – Referral Form</title>
<link href="https://fonts.googleapis.com/css2?family=Source+Sans+3:wght@400;600&display=swap" rel="stylesheet">
<style>
:root{
  --ink:#161616;
  --teal:#1a9ab4;
  --teal-deep:#0c7f9b;
  --teal-light:#5cc3d8;
  --navy:#1e3a58;
  --rule:#8a8a8a;
  --box:#555;
  --panel:#f7fafb;
  --white:#ffffff;
}
*{box-sizing:border-box;margin:0;padding:0}
html,body{width:1200px;height:777px;overflow:hidden;background:#fff}
body{font-family:"Source Sans 3",Arial,sans-serif;color:var(--ink)}
.card{position:relative;width:1200px;height:777px;background:var(--white);overflow:hidden}
.abs{position:absolute}
.side-panel{left:0;top:0;width:282px;height:777px;background:var(--panel);border-right:1px solid #e3e9eb}
.brand{left:22px;top:40px;display:flex;align-items:center;gap:12px}
.brand-mark{width:30px;height:30px;background:var(--teal)}
.brand-name{font-size:24px;line-height:1.05;color:var(--teal);font-weight:600;width:200px}
.label{font-size:17px;line-height:1}
.heading{font-size:17px;text-transform:uppercase;line-height:1}
.rule{height:1px;background:var(--rule)}
.cb{display:inline-block;width:18px;height:18px;border:1.5px solid var(--box);background:#fff;vertical-align:middle}
.cb-row{display:flex;align-items:center;gap:14px;font-size:17px;line-height:1;height:29.4px}
.days{left:22px;top:390px;display:flex;gap:8px}
.day{display:flex;flex-direction:column;align-items:center;gap:6px;width:26px;font-size:13px}
.notice{left:22px;top:452px;width:242px;font-size:16px;line-height:1.26}
.col{display:flex;flex-direction:column}
.chart-row{display:flex;gap:6.6px}
.tooth{display:flex;flex-direction:column;align-items:center;width:18px;font-size:10.5px;gap:4px}
.tooth .cb{width:18px;height:18px;border-width:1px}
.letters{display:flex;border:1px solid var(--box)}
.letters span{width:24.9px;height:22px;border-right:1px solid var(--box);font-size:11px;display:flex;align-items:center;justify-content:center}
.letters span:last-child{border-right:0}
.prim-boxes{display:flex}
.prim-boxes span{width:24.9px;height:22px;display:flex;align-items:center;justify-content:center}
.prim-boxes .cb{width:16px;height:16px;border-width:1px}
.tooth-map{left:852px;top:304px;width:254px;height:124px;background:linear-gradient(180deg,#f2f2f2,#d7dadc);border-radius:6px}
.comments-box{left:667px;top:483px;width:511px;height:156px;border:1.5px solid var(--box)}
.band{left:0;top:0;width:1200px;height:777px;pointer-events:none}
.footer-text{color:var(--white);font-size:17px;line-height:25.5px}
.web{left:0;width:1200px;top:704px;text-align:center;color:var(--white);font-size:24px;letter-spacing:3px}
</style>
</head>
<body>
<main class="card">
  <aside class="abs side-panel"></aside>

  <div class="abs brand">
    <span class="brand-mark"></span>
    <span class="brand-name">Harlow Creek Oral Surgery</span>
  </div>

  <div class="abs heading" style="left:40px;top:163px">Apointment</div>

  <div class="abs label" style="left:26px;top:218px">Date</div>
  <div class="abs rule" style="left:84px;top:234px;width:172px"></div>
  <div class="abs cb-row" style="left:50px;top:270px;gap:12px"><span class="cb"></span>AM<span class="cb" style="margin-left:34px"></span>PM</div>

  <div class="abs label" style="left:26px;top:338px">Time</div>
  <div class="abs rule" style="left:84px;top:354px;width:172px"></div>

  <div class="abs days">
    <div class="day"><span class="cb"></span>Mon</div>
    <div class="day"><span class="cb"></span>Tue</div>
    <div class="day"><span class="cb"></span>Wed</div>
    <div class="day"><span class="cb"></span>Thu</div>
    <div class="day"><span class="cb"></span>Fri</div>
    <div class="day"><span class="cb"></span>Sat</div>
  </div>

  <p class="abs notice">This time is reserved specifically for you. If by necessity, you must cancel your appointment for surgery please notify us at least one day / 24 hours in advance.</p>

  <div class="abs label" style="left:297px;top:26px">Patient' name:</div>
  <div class="abs rule" style="left:440px;top:40px;width:294px"></div>
  <div class="abs label" style="left:777px;top:26px">Date:</div>
  <div class="abs rule" style="left:830px;top:40px;width:344px"></div>
  <div class="abs label" style="left:297px;top:73px">Patient's phone:</div>
  <div class="abs rule" style="left:440px;top:87px;width:294px"></div>
  <div class="abs label" style="left:777px;top:73px">Referred by:</div>
  <div class="abs rule" style="left:880px;top:87px;width:294px"></div>

  <div class="abs col" style="left:297px;top:99px">
    <div class="cb-row"><span class="cb"></span>Wisdom Teeth</div>
    <div class="cb-row"><span class="cb"></span>Extraction</div>
    <div class="cb-row"><span class="cb"></span>Implants</div>
    <div class="cb-row"><span class="cb"></span>Bone Grafting</div>
    <div class="cb-row"><span class="cb"></span>Exposure and bonding</div>
    <div class="cb-row"><span class="cb"></span>Biopsy (Soft or Hard Tissue)</div>
    <div class="cb-row"><span class="cb"></span>Lesion Evaluation</div>
    <div class="cb-row"><span class="cb"></span>Infection (I&amp;D)</div>
    <div class="cb-row"><span class="cb"></span>Alveoloplasty</div>
    <div class="cb-row"><span class="cb"></span>Frenectomy</div>
    <div class="cb-row"><span class="cb"></span>Orthognathic</div>
    <div class="cb-row"><span class="cb"></span>TMJ</div>
    <div class="cb-row"><span class="cb"></span>Other</div>
  </div>

  <div class="abs heading" style="left:297px;top:489px">Surgical Template</div>
  <div class="abs col" style="left:297px;top:512px">
    <div class="cb-row"><span class="cb"></span>To be provided by restorative dentist</div>
    <div class="cb-row"><span class="cb"></span>To be fabricated by the surgeon</div>
    <div class="cb-row"><span class="cb"></span>Other</div>
  </div>

  <div class="abs heading" style="left:603px;top:108px">Implants</div>
  <div class="abs col" style="left:606px;top:131px">
    <div class="cb-row"><span class="cb"></span>Noveline</div>
    <div class="cb-row"><span class="cb"></span>Stellmar</div>
    <div class="cb-row"><span class="cb"></span>Astrin</div>
    <div class="cb-row"><span class="cb"></span>Q3</div>
    <div class="cb-row"><span class="cb"></span>Other</div>
  </div>

  <div class="abs heading" style="left:603px;top:305px">Radiographs</div>
  <div class="abs col" style="left:603px;top:330px">
    <div class="cb-row"><span class="cb"></span>Being Mailed/ emailed</div>
    <div class="cb-row"><span class="cb"></span>Given to the Patient</div>
    <div class="cb-row"><span class="cb"></span>Please take</div>
    <div class="cb-row"><span class="cb"></span>Other</div>
  </div>

  <div class="abs col" style="left:777px;top:108px;gap:8px">
    <div class="chart-row">
      <div class="tooth"><span class="cb"></span>1</div><div class="tooth"><span class="cb"></span>2</div><div class="tooth"><span class="cb"></span>3</div><div class="tooth"><span class="cb"></span>4</div><div class="tooth"><span class="cb"></span>5</div><div class="tooth"><span class="cb"></span>6</div><div class="tooth"><span class="cb"></span>7</div><div class="tooth"><span class="cb"></span>8</div><div class="tooth"><span class="cb"></span>9</div><div class="tooth"><span class="cb"></span>10</div><div class="tooth"><span class="cb"></span>11</div><div class="tooth"><span class="cb"></span>12</div><div class="tooth"><span class="cb"></span>13</div><div class="tooth"><span class="cb"></span>14</div><div class="tooth"><span class="cb"></span>15</div><div class="tooth"><span class="cb"></span>16</div>
    </div>
    <div class="chart-row">
      <div class="tooth"><span class="cb"></span>32</div><div class="tooth"><span class="cb"></span>31</div><div class="tooth"><span class="cb"></span>30</div><div class="tooth"><span class="cb"></span>29</div><div class="tooth"><span class="cb"></span>28</div><div class="tooth"><span class="cb"></span>27</div><div class="tooth"><span class="cb"></span>26</div><div class="tooth"><span class="cb"></span>25</div><div class="tooth"><span class="cb"></span>24</div><div class="tooth"><span class="cb"></span>23</div><div class="tooth"><span class="cb"></span>22</div><div class="tooth"><span class="cb"></span>21</div><div class="tooth"><span class="cb"></span>20</div><div class="tooth"><span class="cb"></span>19</div><div class="tooth"><span class="cb"></span>18</div><div class="tooth"><span class="cb"></span>17</div>
    </div>
  </div>

  <div class="abs col" style="left:847px;top:194px">
    <div class="prim-boxes"><span><i class="cb"></i></span><span><i class="cb"></i></span><span><i class="cb"></i></span><span><i class="cb"></i></span><span><i class="cb"></i></span><span><i class="cb"></i></span><span><i class="cb"></i></span><span><i class="cb"></i></span><span><i class="cb"></i></span><span><i class="cb"></i></span></div>
    <div class="letters"><span>A</span><span>B</span><span>C</span><span>D</span><span>E</span><span>F</span><span>G</span><span>H</span><span>I</span><span>J</span></div>
    <div class="prim-boxes" style="margin-top:4px"><span><i class="cb"></i></span><span><i class="cb"></i></span><span><i class="cb"></i></span><span><i class="cb"></i></span><span><i class="cb"></i></span><span><i class="cb"></i></span><span><i class="cb"></i></span><span><i class="cb"></i></span><span><i class="cb"></i></span><span><i class="cb"></i></span></div>
    <div class="letters"><span>T</span><span>S</span><span>R</span><span>Q</span><span>P</span><span>O</span><span>N</span><span>M</span><span>L</span><span>K</span></div>
  </div>

  <div class="abs tooth-map" role="img" aria-label="Tooth map diagram of upper and lower arches, marked right and left"></div>

  <div class="abs heading" style="left:671px;top:462px">Additional Comments</div>
  <div class="abs comments-box"></div>

  <svg class="abs band" viewBox="0 0 1200 777" aria-hidden="true">
    <defs>
      <linearGradient id="bandFill" x1="0" y1="0" x2="1" y2="0">
        <stop offset="0" stop-color="#1b9ab5"/>
        <stop offset="0.5" stop-color="#27acc6"/>
        <stop offset="1" stop-color="#0d86a2"/>
      </linearGradient>
    </defs>
    <path d="M0 652 C 260 690 560 700 820 680 C 980 668 1100 650 1200 640 L1200 777 L0 777 Z" fill="url(#bandFill)"/>
    <path d="M0 672 C 300 712 650 716 900 692 C 1030 680 1130 664 1200 656 L1200 664 C 1120 674 1020 690 900 702 C 640 726 300 724 0 684 Z" fill="#7fd3e3" opacity="0.55"/>
  </svg>

  <div class="abs footer-text" style="left:22px;top:668px">2210 Alder Lane<br>Fairview, NE 68000<br>Tel (555) 014 2270<br>Fax (555) 014 2271</div>
  <div class="abs web">www.kreldax.com</div>
  <div class="abs footer-text" style="right:22px;top:688px;text-align:right">Save time<br>fill out patient registration<br>health hisory online</div>
</main>
</body>
</html>
```